Used Semi Truck Website Redesign

We are redoing the website backend and would like to also do a front end redesign. I would like a Mobile and Desktop mockup for each page. The website has more mobile visitors than desktop visitors. Our competitor is http://www.haulmarketbay.example. We don't want to copy them exactly but we want a site that looks more like that. We need the functionality of that site. One big difference is that we also sell parts and trailers.

We need a redesign for front page, product detail page, search result page, content page. It is very important that the site is very easy to use on mobile devices. Our target audience is Truck drivers.

Feel free to use demo fonts stock images, and icons. We will purchase necessary 3rd party media when a winner is chosen.

Target Market(s)

People who want to buy used trucks.

Coding

Coded - Design and coding required

Number of Pages Required

5+ page

Requirements
Must have
• Mockup for Desktop and Mobile pages.

```html
<!DOCTYPE html>
<html lang="en">
<head>
<meta charset="utf-8">
<title>Trucks For Sale</title>
<link href="https://fonts.googleapis.com/css2?family=Roboto:wght@400;500;700&display=swap" rel="stylesheet">
<style>
:root{
  --navy:#0a2a8a;
  --band:#0b3399;
  --deep:#082470;
  --orange:#f7941d;
  --panel:#f1f1f1;
  --card:#f7f7f7;
  --text:#333;
  --muted:#666;
  --link:#1a44a8;
  --line:#fff;
  --feed:#3aa0dd;
}
*{box-sizing:border-box;margin:0;padding:0}
html,body{width:679px;height:1200px;overflow:hidden;background:#fff;font-family:Roboto,Arial,sans-serif;color:var(--text)}
.page{position:relative;width:679px;height:1200px}
.topbar{position:absolute;top:0;left:0;width:679px;height:20px;background:var(--navy);color:#fff;font-size:7px;display:flex;align-items:center;justify-content:space-between;padding:0 50px}
.header{position:absolute;top:20px;left:0;width:679px;height:33px;display:flex;align-items:center;justify-content:space-between;padding:0 50px}
.brand{font-size:17px;font-weight:400;color:var(--navy)}
.nav{display:flex;align-items:center;gap:9px;font-size:7.5px;color:#333}
.social{display:flex;gap:3px}
.social span{width:13px;height:13px;border-radius:50%;display:block}
.search{position:absolute;top:53px;left:0;width:679px;height:53px;background:var(--band);padding:0 50px}
.search .label{color:#fff;font-size:7px;margin-top:10px}
.search .row{display:flex;gap:4px;margin-top:2px}
.field{height:18px;background:#fff;font-size:6px;color:#999;display:flex;align-items:center;justify-content:space-between;padding:0 6px}
.field.sel::after{content:"";border:2px solid transparent;border-top:2.5px solid #444;margin-top:2px}
.btn-search{width:54px;height:18px;background:var(--orange);color:#fff;font-size:7px;display:flex;align-items:center;justify-content:center}
.crumb{position:absolute;top:125px;left:50px;font-size:7px;color:var(--link)}
.title{position:absolute;top:134px;left:50px;font-size:11.5px;font-weight:500}
.sidebar{position:absolute;top:154px;left:50px;width:180px;background:var(--panel)}
.srow{border-bottom:1px solid var(--line);padding:0 10px;position:relative}
.shead{font-size:7.5px;color:#333;display:flex;align-items:center;gap:4px}
.shead .car{border:2px solid transparent;border-top:2.5px solid #555;margin-top:2px}
.upd{position:absolute;right:10px;width:49px;height:18px;background:var(--navy);color:#fff;font-size:7px;display:flex;align-items:center;justify-content:center;gap:3px;font-weight:500}
.upd b{font-size:9px;font-weight:700;line-height:1}
.inp{height:18px;background:#fff;border:1px solid #ddd;font-size:6px;color:#aaa;display:flex;align-items:center;padding:0 6px;white-space:nowrap}
.chk{font-size:6px;color:#777;display:flex;align-items:center;gap:3px;line-height:10px}
.box{width:6px;height:6px;border:1px solid #ccc;background:#fff;display:inline-block;flex:none}
.box.on{background:var(--link);border-color:var(--link)}
.cls{font-size:6px;display:flex;align-items:center;gap:4px;line-height:12px;white-space:nowrap}
.cls a{color:var(--link);text-decoration:none;width:60px}
.cls i{font-style:normal;color:#888}
.card{position:absolute;left:242px;width:388px;height:137.6px;background:var(--card)}
.photo{position:absolute;left:0;top:0;width:147px;height:137.6px}
.body{position:absolute;left:159px;top:12px;width:220px}
.body h2{font-size:11px;font-weight:400;color:#222}
.body p{font-size:6.6px;color:var(--muted);line-height:10px;margin-top:5px}
.spec{font-size:6.6px;line-height:11px;margin-top:4px}
.spec div{display:flex}
.spec dt{color:var(--link);width:45px}
.spec dd{color:#555}
.actions{position:absolute;left:159px;top:106px;display:flex;gap:6px}
.actions span{height:18px;font-size:6.8px;color:#fff;display:flex;align-items:center;justify-content:center}
.a1{width:80px;background:var(--orange)}
.a2{width:68px;background:var(--navy)}
.footer{position:absolute;top:1018px;left:0;width:679px;height:156px;background:var(--band);color:#fff}
.footer h3{font-size:9.5px;font-weight:500;position:absolute;top:18px}
.post{position:absolute;display:flex;gap:6px;width:170px}
.thumb{width:35px;height:32px;flex:none}
.post b{font-size:6.6px;font-weight:500;display:block}
.post .date{font-size:5.8px;color:var(--orange);margin:2px 0}
.post small{font-size:5.8px;line-height:8px;display:block}
.tw{position:absolute;display:flex;gap:6px;width:160px}
.tw .sq{width:26px;height:26px;background:var(--feed);flex:none}
.tw b{font-size:6.6px;font-weight:500;display:block;margin-bottom:2px}
.tw small{font-size:5.8px;line-height:8px;display:block}
.tw .meta{position:absolute;top:29px;left:0;font-size:6.2px;display:flex;gap:6px;width:200px}
.links{position:absolute;top:42px;left:496px;display:grid;grid-template-columns:69px 80px;font-size:6px;line-height:12px}
.copy{position:absolute;top:1174px;left:0;width:679px;height:26px;background:var(--deep);color:#fff;font-size:6.6px;display:flex;align-items:center;justify-content:center}
</style>
</head>
<body>
<div class="page">
  <div class="topbar"><span>256, 140 Trucks and trailers For Sale</span><span>My Trader:&nbsp;&nbsp; Login | Register | Find aDealer | Dealer Login</span></div>

  <header class="header">
    <div class="brand">Logo Here</div>
    <nav class="nav"><span>Find</span><span>Sell</span><span>Research</span>
      <div class="social"><span style="background:#3b5998"></span><span style="background:#1da1f2"></span><span style="background:#dd4b39"></span><span style="background:#0e3a7a"></span></div>
    </nav>
  </header>

  <section class="search">
    <div class="label">Quick Search</div>
    <div class="row">
      <div class="field" style="width:96px">Keyword</div>
      <div class="field sel" style="width:96px">Select a Class</div>
      <div class="field sel" style="width:96px">Select a Category</div>
      <div class="field sel" style="width:96px">Select a Make</div>
      <div class="field" style="width:54px">Zip Code</div>
      <div class="field sel" style="width:64px">Any Distance</div>
      <div class="btn-search">Search</div>
    </div>
  </section>

  <div class="crumb">Home</div>
  <h1 class="title">Trucks For Sale</h1>

  <aside class="sidebar">
    <div class="srow" style="height:37.6px"><div class="shead" style="padding-top:15px">Refine Search</div><div class="upd" style="top:10px">Clear All</div></div>
    <div class="srow" style="height:51px"><div class="shead" style="padding-top:10px">Keyword <span class="car"></span></div><div class="inp" style="width:80px;margin-top:4px">Keyword</div><div class="upd" style="top:24px"><b>+</b> Update</div></div>
    <div class="srow" style="height:66px"><div class="shead" style="padding-top:10px">Location <span class="car"></span></div>
      <div class="chk"><span class="box on"></span>Zip <span class="box"></span>US States</div>
      <div style="display:flex;gap:3px;margin-top:7px"><div class="inp" style="width:40px">Zip Code</div><div class="inp" style="width:60px;justify-content:space-between">within 500 mi <span style="border:2px solid transparent;border-top:2.5px solid #555;margin-top:2px"></span></div></div>
      <div class="upd" style="top:37px"><b>+</b> Update</div></div>
    <div class="srow" style="height:46px"><div class="shead" style="padding-top:8px">Location <span class="car"></span></div>
      <div class="chk"><span class="box on"></span>New ( 152, 985)</div><div class="chk"><span class="box"></span>Used (104, 003)</div>
      <div class="upd" style="top:20px"><b>+</b> Update</div></div>
    <div class="srow" style="height:50px"><div class="shead" style="padding-top:9px">Mileage <span class="car"></span></div>
      <div style="display:flex;gap:3px;margin-top:4px"><div class="inp" style="width:40px">From</div><div class="inp" style="width:34px">To</div></div><div class="upd" style="top:22px"><b>+</b> Update</div></div>
    <div class="srow" style="height:50px"><div class="shead" style="padding-top:9px">Model Years <span class="car"></span></div>
      <div style="display:flex;gap:3px;margin-top:4px"><div class="inp" style="width:40px">From</div><div class="inp" style="width:34px">To</div></div><div class="upd" style="top:22px"><b>+</b> Update</div></div>
    <div class="srow" style="height:74px"><div class="shead" style="padding-top:9px">Price <span class="car"></span></div>
      <div style="display:flex;gap:3px;margin-top:4px"><div class="inp" style="width:40px">From</div><div class="inp" style="width:34px">To</div></div>
      <div class="chk" style="margin-top:4px"><span class="box on"></span>Accepting Offers</div><div class="chk"><span class="box"></span>For Lease</div>
      <div class="upd" style="top:22px"><b>+</b> Update</div></div>
    <div class="srow" style="height:110px"><div class="shead" style="padding-top:10px;margin-bottom:6px">Class <span class="car"></span></div>
      <div class="cls"><span class="box"></span><a>Heavy Duty</a><i>(46,090)</i></div>
      <div class="cls"><span class="box"></span><a>Medium Duty</a><i>(28,998)</i></div>
      <div class="cls"><span class="box"></span><a>Light Duty</a><i>(155,651)</i></div>
      <div class="cls"><span class="box"></span><a>Trailer</a><i>(24,664)</i></div>
      <div class="cls"><span class="box"></span><a>Truck Body</a><i>(1,094)</i></div>
      <div class="cls"><span class="box"></span><a>Storage Buildings</a><i>(74)</i></div>
      <div class="upd" style="top:5px"><b>+</b> Update</div></div>
    <div class="srow" style="height:29.3px"><div class="shead" style="padding-top:10px">Category <span class="car"></span></div><div class="upd" style="top:5px"><b>+</b> Update</div></div>
    <div class="srow" style="height:29.3px"><div class="shead" style="padding-top:10px">Truck Manufacturer <span class="car"></span></div><div class="upd" style="top:5px"><b>+</b> Update</div></div>
    <div class="srow" style="height:29.3px"><div class="shead" style="padding-top:10px">Upfit Manufacturer <span class="car"></span></div><div class="upd" style="top:5px"><b>+</b> Update</div></div>
    <div class="srow" style="height:29.3px"><div class="shead" style="padding-top:10px">Upfit Body Type <span class="car"></span></div><div class="upd" style="top:5px"><b>+</b> Update</div></div>
    <div class="srow" style="height:29.3px"><div class="shead" style="padding-top:10px">Cab Type <span class="car"></span></div><div class="upd" style="top:5px"><b>+</b> Update</div></div>
    <div class="srow" style="height:29.3px"><div class="shead" style="padding-top:10px">Tagline <span class="car"></span></div><div class="upd" style="top:5px"><b>+</b> Update</div></div>
    <div class="srow" style="height:29.3px"><div class="shead" style="padding-top:10px">Drivetrain <span class="car"></span></div><div class="upd" style="top:5px"><b>+</b> Update</div></div>
    <div class="srow" style="height:29.3px"><div class="shead" style="padding-top:10px">Engine Type <span class="car"></span></div><div class="upd" style="top:5px"><b>+</b> Update</div></div>
    <div class="srow" style="height:29.3px"><div class="shead" style="padding-top:10px">Engine Size <span class="car"></span></div><div class="upd" style="top:5px"><b>+</b> Update</div></div>
    <div class="srow" style="height:29.3px"><div class="shead" style="padding-top:10px">Transmission Type <span class="car"></span></div><div class="upd" style="top:5px"><b>+</b> Update</div></div>
    <div class="srow" style="height:29.3px"><div class="shead" style="padding-top:10px">Transmission Speed <span class="car"></span></div><div class="upd" style="top:5px"><b>+</b> Update</div></div>
    <div class="srow" style="height:29.3px;border-bottom:0"><div class="shead" style="padding-top:10px">Fuel Type <span class="car"></span></div><div class="upd" style="top:5px"><b>+</b> Update</div></div>
  </aside>

  <article class="card" style="top:126.4px">
    <div class="photo" role="img" aria-label="White semi truck with flatbed trailer at a yard" style="background:linear-gradient(180deg,#7fa6c9 0%,#c9d3da 45%,#8a8f93 100%)"></div>
    <div class="body"><h2>Truck name goes here</h2><p>Etiam rhoncus. Maecenas tempus, tellus eget condimentum rhoncus, sem quam semper libero, sit amet adipiscing sem neque sed ipsum lorem ipsum.</p>
      <dl class="spec"><div><dt>Condition:</dt><dd>New</dd></div><div><dt>Engine size:</dt><dd>5.1</dd></div><div><dt>Fuel Type:</dt><dd>Diesel</dd></div></dl></div>
    <div class="actions"><span class="a1">View Contact Info</span><span class="a2">View More Info</span></div>
  </article>
  <article class="card" style="top:272px">
    <div class="photo" role="img" aria-label="Yellow loader on a dump truck under a blue sky" style="background:linear-gradient(180deg,#4f7fb8 0%,#a9bdd0 50%,#7d7a70 100%)"></div>
    <div class="body"><h2>Truck name goes here</h2><p>Etiam rhoncus. Maecenas tempus, tellus eget condimentum rhoncus, sem quam semper libero, sit amet adipiscing sem neque sed ipsum lorem ipsum.</p>
      <dl class="spec"><div><dt>Condition:</dt><dd>New</dd></div><div><dt>Engine size:</dt><dd>5.1</dd></div><div><dt>Fuel Type:</dt><dd>Diesel</dd></div></dl></div>
    <div class="actions"><span class="a1">View Contact Info</span><span class="a2">View More Info</span></div>
  </article>
  <article class="card" style="top:418.4px">
    <div class="photo" role="img" aria-label="Front view of a white semi truck in a parking lot" style="background:linear-gradient(180deg,#9fb4c4 0%,#d6dadc 45%,#56595c 100%)"></div>
    <div class="body"><h2>Truck name goes here</h2><p>Etiam rhoncus. Maecenas tempus, tellus eget condimentum rhoncus, sem quam semper libero, sit amet adipiscing sem neque sed ipsum lorem ipsum.</p>
      <dl class="spec"><div><dt>Condition:</dt><dd>New</dd></div><div><dt>Engine size:</dt><dd>5.1</dd></div><div><dt>Fuel Type:</dt><dd>Diesel</dd></div></dl></div>
    <div class="actions"><span class="a1">View Contact Info</span><span class="a2">View More Info</span></div>
  </article>
  <article class="card" style="top:564px">
    <div class="photo" role="img" aria-label="Red semi truck with flatbed on an open highway" style="background:linear-gradient(180deg,#3f6fa8 0%,#b8c6d2 45%,#8a7a5e 75%,#4a4540 100%)"></div>
    <div class="body"><h2>Truck name goes here</h2><p>Etiam rhoncus. Maecenas tempus, tellus eget condimentum rhoncus, sem quam semper libero, sit amet adipiscing sem neque sed ipsum lorem ipsum.</p>
      <dl class="spec"><div><dt>Condition:</dt><dd>New</dd></div><div><dt>Engine size:</dt><dd>5.1</dd></div><div><dt>Fuel Type:</dt><dd>Diesel</dd></div></dl></div>
    <div class="actions"><span class="a1">View Contact Info</span><span class="a2">View More Info</span></div>
  </article>
  <article class="card" style="top:709.6px">
    <div class="photo" role="img" aria-label="Dark red truck with box trailer under a station canopy" style="background:linear-gradient(180deg,#5d7a8a 0%,#9aa9ae 45%,#4d4a4c 100%)"></div>
    <div class="body"><h2>Truck name goes here</h2><p>Etiam rhoncus. Maecenas tempus, tellus eget condimentum rhoncus, sem quam semper libero, sit amet adipiscing sem neque sed ipsum lorem ipsum.</p>
      <dl class="spec"><div><dt>Condition:</dt><dd>New</dd></div><div><dt>Engine size:</dt><dd>5.1</dd></div><div><dt>Fuel Type:</dt><dd>Diesel</dd></div></dl></div>
    <div class="actions"><span class="a1">View Contact Info</span><span class="a2">View More Info</span></div>
  </article>
  <article class="card" style="top:856px">
    <div class="photo" role="img" aria-label="Road train truck driving on an outback road" style="background:linear-gradient(180deg,#6f89a8 0%,#b5b3ad 45%,#8a6a4f 70%,#5b5550 100%)"></div>
    <div class="body"><h2>Truck name goes here</h2><p>Etiam rhoncus. Maecenas tempus, tellus eget condimentum rhoncus, sem quam semper libero, sit amet adipiscing sem neque sed ipsum lorem ipsum.</p>
      <dl class="spec"><div><dt>Condition:</dt><dd>New</dd></div><div><dt>Engine size:</dt><dd>5.1</dd></div><div><dt>Fuel Type:</dt><dd>Diesel</dd></div></dl></div>
    <div class="actions"><span class="a1">View Contact Info</span><span class="a2">View More Info</span></div>
  </article>

  <footer class="footer">
    <h3 style="left:68px">Commercial Truck Blog</h3>
    <div class="post" style="left:68px;top:43px"><div class="thumb" role="img" aria-label="Truck blog post thumbnail" style="background:linear-gradient(180deg,#c8ccd2,#7c7468)"></div>
      <div><b>Lorem ipsum dolor sit amet.</b><div class="date">&#9638; 24th November</div><small>Lorem ipsum dolor sit amet, consectetur adipiscing elit, sed do eiusmod.</small></div></div>
    <div class="post" style="left:68px;top:96px"><div class="thumb" role="img" aria-label="Blue truck blog post thumbnail" style="background:linear-gradient(180deg,#4a6fb5,#1c2e6a)"></div>
      <div><b>Lorem ipsum dolor sit amet.</b><div class="date">&#9638; 24th November</div><small>Lorem ipsum dolor sit amet, consectetur adipiscing elit, sed do eiusmod.</small></div></div>

    <h3 style="left:263px">Road Chatter Feed</h3>
    <div class="tw" style="left:263px;top:43px"><div class="sq"></div><div><b>Lorem ipsum dolor sit amet.</b><small>Lorem ipsum dolor sit amet, consectetur adipiscing elit, sed do eiusmod.</small></div>
      <div class="meta"><span>&#8635; Reshare</span><span>&#9733; Favorite</span></div></div>
    <div class="tw" style="left:263px;top:96px"><div class="sq"></div><div><b>Lorem ipsum dolor sit amet.</b><small>Lorem ipsum dolor sit amet, consectetur adipiscing elit, sed do eiusmod.</small></div>
      <div class="meta"><span>&#8635; Reshare</span><span style="color:var(--orange)">&#9733; Favorite</span></div></div>

    <h3 style="left:496px">Quick Links</h3>
    <div class="links">
      <span>Insurance</span><span>Truck Parts</span>
      <span>Jobs &amp; Training</span><span>Steel Buildings</span>
      <span>Vehicle History</span><span>Fuel Management</span>
      <span>Truck Bodies</span><span>Shipping &amp; Transport</span>
      <span>Finance/Lease</span><span></span>
    </div>
  </footer>
  <div class="copy">Copyright 2016&nbsp; All Rights Reserved</div>
</div>
</body>
</html>
```